The Tidegrove Newsletter For My Monthly Investment Newsletters

I'm looking to create two beautiful newsletter template for my new financial planning and investment firm. I keep my newsletters short and sweet as I feel less is more. One newsletter is for investment updates - I send that to clients and prospects. The other is more of an update for clients only.

I'm going to be using Mailchimp & Constant Contact so please make sure I can use that template there.

My newsletter typically goes out monthly. There are two versions - one for clients and one for prospects. Sometimes, information is applicable for clients only.

The newsletter brief should have the month and year in it like
The Tidegrove Newsletter: March 2020.

The other can be

The Tidegrove Update: March 2020 (for more administrative announcements).

Target Market(s)

Investors

Industry/Entity Type

Investment Advisory

Font styles to use
Sans Serif

Colors

Designer to choose colors to be used in the design.

Requirements
Must have
• Clean
• professional
• Modern feel
• Less is more.
• Colors should match and be in sync my logo.
• I'm going to be using Mailchimp & Constant Contact so please make sure I can use that template there.
Nice to have
• Please follow the must haves

```html
<!DOCTYPE html>
<html lang="en">
<head>
<meta charset="utf-8">
<title>The Tidegrove Newsletter · March 2020</title>
<link href="https://fonts.googleapis.com/css2?family=Open+Sans:wght@400;600;700&display=swap" rel="stylesheet">
<style>
  :root{
    --page:#eef0f3;
    --card:#ffffff;
    --navy:#163a5c;
    --orange:#f4892a;
    --blue:#2a73b8;
    --ink:#1f2f40;
    --text:#5b6470;
    --muted:#8a929c;
    --line:#dfe3e8;
    --footer:#f2f4f6;
  }
  *{box-sizing:border-box;margin:0;padding:0}
  html,body{width:774px;height:1200px;overflow:hidden}
  body{background:var(--page);font-family:"Open Sans",Arial,sans-serif;color:var(--text)}
  .newsletter{width:600px;margin:0 auto;}
  .preheader{height:30px;font-size:10px;color:var(--muted);text-align:center;line-height:30px}
  .preheader a{color:var(--blue);text-decoration:underline}
  .masthead{background:var(--card);height:84px;display:flex;align-items:center;justify-content:space-between;padding:0 32px}
  .brand{display:flex;align-items:center;gap:10px;color:var(--navy);font-weight:700;font-size:20px}
  .brand-dot{width:14px;height:14px;border-radius:50%;background:var(--navy)}
  .btn{display:inline-block;background:var(--orange);color:#fff;font-weight:700;font-size:11px;letter-spacing:.06em;text-transform:uppercase;padding:11px 18px;text-decoration:none}
  .issue-band{background:var(--navy);color:#fff;height:40px;display:flex;align-items:center;justify-content:space-between;padding:0 32px;font-size:15px;font-weight:600}
  .issue-band .date{font-weight:700}
  .content{background:var(--card);padding:26px 32px 10px}
  .issue-title{font-size:22px;color:var(--ink);font-weight:700}
  .issue-sub{font-size:12px;color:var(--text);margin-top:4px;font-weight:600}
  .topic{margin-top:22px}
  .topic-head{display:flex;align-items:center;gap:10px;font-size:14px;font-weight:700;color:var(--ink)}
  .topic-head svg{flex:none}
  .topic p,.notice p,.feature p{font-size:12px;line-height:1.65;margin-top:10px}
  .topic a{color:var(--blue);text-decoration:underline}
  .feature{margin:26px 0 10px;border:1px solid var(--line);padding:24px 28px 26px}
  .feature h2{font-size:20px;color:var(--ink);font-weight:700}
  .feature .btn{margin-top:16px}
  .notice{background:var(--card);padding:14px 32px 26px}
  .notice h2{font-size:17px;line-height:1.45;color:var(--blue);font-weight:700}
  .site-footer{background:var(--footer);padding:22px 32px 20px}
  .footer-name{font-size:20px;font-weight:700;color:var(--navy)}
  .footer-tag{font-size:11px;color:var(--blue);margin-top:2px}
  .footer-contacts{display:flex;justify-content:space-between;margin-top:18px;font-size:11px;color:var(--text);line-height:1.5}
  .contact{display:flex;gap:8px;align-items:flex-start}
  .footer-bar{background:var(--navy);height:42px;display:flex;align-items:center;justify-content:space-between;padding:0 32px;font-size:11px}
  .footer-bar a{color:#fff;text-decoration:underline}
</style>
</head>
<body>
<div class="newsletter">
  <div class="preheader">Having trouble viewing this email? <a href="#">View in your browser</a></div>

  <header class="masthead">
    <div class="brand"><span class="brand-dot"></span>The Tidegrove LLC</div>
    <a class="btn" href="#">Schedule a meeting</a>
  </header>

  <div class="issue-band">
    <span>The Tidegrove Newsletter</span>
    <span class="date">• March 2020</span>
  </div>

  <main class="content">
    <h1 class="issue-title">Monthly Economic &amp; Market Analysis</h1>
    <p class="issue-sub">Lorem ipsum dolor sit amet consectetur adipiscing elit</p>

    <section class="topic">
      <div class="topic-head">
        <svg width="20" height="18" viewBox="0 0 20 18" fill="none" stroke="#f4892a" stroke-width="2" stroke-linecap="round" stroke-linejoin="round"><path d="M1 17h18"/><path d="M2 13l5-5 4 3 7-8"/><path d="M14 3h4v4"/></svg>
        Consectetur adipiscing elit
      </div>
      <p>Markets ended the month on steadier footing as inflation data cooled and bond yields eased. Equities recovered much of the early decline, led by healthcare and utilities, while energy lagged. We continue to favor broad diversification and a measured approach to new positions. <a href="#">Read the full report</a></p>
    </section>

    <section class="topic">
      <div class="topic-head">
        <svg width="20" height="18" viewBox="0 0 20 18" fill="none" stroke="#f4892a" stroke-width="2" stroke-linecap="round"><path d="M7 3h12M7 9h12M7 15h12"/><circle cx="2" cy="3" r="1" fill="#f4892a"/><circle cx="2" cy="9" r="1" fill="#f4892a"/><circle cx="2" cy="15" r="1" fill="#f4892a"/></svg>
        Semper semper tristique
      </div>
      <p>Interest rates remain a key focus for the months ahead. Our team is reviewing cash reserves, bond ladders and retirement income plans to make sure each portfolio stays aligned with your goals and time horizon. <a href="#">See our outlook</a>.</p>
    </section>

    <section class="feature">
      <h2>Investing locally in new bussnies</h2>
      <p>Local businesses are finding new ways to grow, and community investment can play a meaningful role in a balanced plan. Learn how we evaluate regional opportunities and manage the risks that come with them.</p>
      <a class="btn" href="#">Learn more</a>
    </section>
  </main>

  <section class="notice">
    <h2>Ultrices massa in non mollis bibendum lorem velit fames. Nec penatibus adipiscing ultricies urna</h2>
    <p>Tax season is approaching, so now is a good time to gather statements and review contributions. Please reach out if your income, family or employment has changed this year so we can update your plan before filing deadlines.</p>
  </section>

  <footer>
    <div class="site-footer">
      <div class="footer-name">The Tidegrove LLC</div>
      <div class="footer-tag">Financial Planning &amp; Investment Advisory</div>
      <div class="footer-contacts">
        <div class="contact">
          <svg width="12" height="16" viewBox="0 0 12 16"><path d="M6 0a6 6 0 0 0-6 6c0 4.5 6 10 6 10s6-5.5 6-10a6 6 0 0 0-6-6z" fill="#163a5c"/><circle cx="6" cy="6" r="2.2" fill="#f2f4f6"/></svg>
          <div>482 Harbor Lane<br>Suite 12, Easton, CT 06612</div>
        </div>
        <div class="contact">
          <svg width="14" height="14" viewBox="0 0 24 24"><path d="M6.6 10.8a15.1 15.1 0 0 0 6.6 6.6l2.2-2.2a1 1 0 0 1 1-.25 11.4 11.4 0 0 0 3.6.57 1 1 0 0 1 1 1V20a1 1 0 0 1-1 1A17 17 0 0 1 3 4a1 1 0 0 1 1-1h3.5a1 1 0 0 1 1 1c0 1.25.2 2.45.57 3.57a1 1 0 0 1-.25 1z" fill="#163a5c"/></svg>
          <div>Phone: (555) 010-0142 | Fax: (555) 010-0143</div>
        </div>
      </div>
    </div>
    <div class="footer-bar">
      <a href="#">Unsubscribe here</a>
      <a href="#">hello@tidegrove-mail.com</a>
    </div>
  </footer>
</div>
</body>
</html>
```